This book will apply the 12 Steps to gaming addiction, also known as video game addiction. The primary purpose of the book is to provide an effective solution for this new type of addiction. The solution is based on the rich and successful concepts of traditional twelve-step programs like RL.

The title on the cover will be "Nine Doors Past the Glowing Screen" and "by Martin Quorby". A subtitle can be used if it works in your design of "A Practical Path Beyond Compulsive Console Play". Cover will be for a 6" x 9" book approximately 110 pages in length.

Some back cover text including some review quotes and an author bio are in the attached Word doc. There is also an author photo attached for for the back cover.

Requirements
Must have
• For the cover design it could be stylized, or an image, a partial image, or whatever. I am open to suggestions. Think about what would be noticed by a person searching for help with moderating their video game use, or by the parents or loved ones of problem gamers. Something contemporary and eye catching.

```html
<!DOCTYPE html>
<html lang="en">
<head>
<meta charset="utf-8">
<title>Nine Doors Past the Glowing Screen — Cover</title>
<link rel="stylesheet" href="https://fonts.googleapis.com/css2?family=Montserrat:ital,wght@0,500;0,600;0,800;0,900;1,700&display=swap">
<style>
  :root {
    --page-bg: #ffffff;
    --cover-yellow: #e9b324;
    --cover-yellow-deep: #dca01a;
    --cover-yellow-light: #f0c23a;
    --ink: #111111;
    --paper: #ffffff;
    --band: #050505;
  }
  * { margin: 0; padding: 0; box-sizing: border-box; }
  html, body {
    width: 1200px;
    height: 960px;
    overflow: hidden;
    background: var(--page-bg);
  }
  .canvas {
    position: relative;
    width: 1200px;
    height: 960px;
  }
  .book-cover {
    position: absolute;
    left: 300px;
    top: 30px;
    width: 600px;
    height: 900px;
    background: radial-gradient(ellipse at 50% 35%, var(--cover-yellow-light) 0%, var(--cover-yellow) 55%, var(--cover-yellow-deep) 100%);
    font-family: 'Montserrat', sans-serif;
    text-align: center;
    overflow: hidden;
  }
  .title-lead {
    position: absolute;
    top: 58px;
    left: 0;
    right: 0;
    font-weight: 800;
    font-size: 30px;
    letter-spacing: 1px;
    color: var(--ink);
  }
  .title-hero {
    position: absolute;
    top: 88px;
    left: 0;
    right: 0;
    font-weight: 800;
    font-size: 128px;
    line-height: 1;
    letter-spacing: -3px;
    color: var(--paper);
  }
  .title-divider {
    position: absolute;
    top: 232px;
    left: 40px;
    right: 40px;
    display: flex;
    align-items: center;
    gap: 18px;
  }
  .title-divider .rule {
    flex: 1;
    height: 3px;
    background: var(--paper);
  }
  .title-divider .joiner {
    font-weight: 700;
    font-style: italic;
    font-size: 28px;
    color: var(--ink);
  }
  .title-main {
    position: absolute;
    top: 272px;
    left: 0;
    right: 0;
    font-weight: 900;
    color: var(--ink);
    line-height: 0.98;
    letter-spacing: -1px;
  }
  .title-main .line-one { display: block; font-size: 66px; }
  .title-main .line-two { display: block; font-size: 86px; }
  .subtitle {
    position: absolute;
    top: 462px;
    left: 40px;
    right: 40px;
    font-weight: 500;
    font-size: 25px;
    line-height: 1.3;
    color: var(--paper);
  }
  .cover-art {
    position: absolute;
    top: 548px;
    left: 60px;
    width: 480px;
    height: 262px;
    background: radial-gradient(ellipse at 50% 60%, #c9946a 0%, #b8873f 45%, rgba(220,160,26,0) 80%);
  }
  .author-band {
    position: absolute;
    left: 0;
    right: 0;
    bottom: 0;
    height: 92px;
    background: var(--band);
    display: flex;
    align-items: center;
    justify-content: center;
  }
  .author-name {
    font-weight: 800;
    font-size: 34px;
    letter-spacing: 3px;
    color: var(--paper);
    text-transform: uppercase;
  }
</style>
</head>
<body>
<div class="canvas">
  <section class="book-cover">
    <div class="title-lead">NINE</div>
    <h1 class="title-hero">DOORS</h1>
    <div class="title-divider">
      <span class="rule"></span>
      <span class="joiner">past the</span>
      <span class="rule"></span>
    </div>
    <h2 class="title-main">
      <span class="line-one">GLOWING</span>
      <span class="line-two">SCREEN</span>
    </h2>
    <p class="subtitle">A Practical Path Beyond<br>Compulsive Console Play</p>
    <div class="cover-art" role="img" aria-label="Photograph of two raised fists with wrists bound by a game controller cable, the controller blurred beside them"></div>
    <div class="author-band">
      <span class="author-name">Martin Quorby</span>
    </div>
  </section>
</div>
</body>
</html>
```